Business Card Design Project

I need a new business card for side business. Very simple and to the point. I am a licensed massage therapist and want the colors to be warm. I don't have a logo or company name. I just need to convey that I am a Licensed Massage Therapist and have my contact information so people can contact me. I'll attach some files that I like. I am a male so I don't want it to be feminine.

One file is my existing card. I like Tessa's card and the layout so would prefer a similar layout. I would like to incorporate my swimmer/biker/runner image. Doesn't have to be the exact likeness because I don't have that file but something similar to that. I would like to also include my areas of specialty of: Swedish, Deep Tissue, Sports, and Hot Stone

I would also like to incorporate a QR code on the back of the card centered.
Updates

Payment is NOW guaranteed to the design I choose.  I updated my creative brief so hopefully it is more clear.  

Industry/Entity Type

Massage

Requirements
Must have
• Glen Harwick
Licensed Massage Therapist
or
Massage Therapy
203-555-0147
gharwick@mailbrook.example

```html
<!DOCTYPE html>
<html lang="en">
<head>
<meta charset="utf-8">
<title>Glen Harwick – Licensed Massage Therapist</title>
<link rel="stylesheet" href="https://fonts.googleapis.com/css2?family=Aladin&display=swap">
<style>
  :root {
    --stone-light: #e3cfb2;
    --stone-mid: #b08d6a;
    --stone-dark: #6e4c34;
    --band: rgba(74, 38, 22, 0.92);
    --panel-top: #b5552c;
    --panel-bottom: #8e3e1f;
    --panel-glow: #c96a3d;
    --ink-light: #fbf3e6;
    --icon-tone: #4a2314;
  }
  html, body {
    margin: 0;
    padding: 0;
    overflow: hidden;
    background: #ffffff;
  }
  .card {
    position: relative;
    width: 1200px;
    height: 720px;
    overflow: hidden;
    font-family: "Aladin", "Papyrus", fantasy;
    color: var(--ink-light);
  }
  .pebble-field {
    position: absolute;
    left: 0;
    top: 0;
    width: 843px;
    height: 720px;
    background:
      radial-gradient(ellipse 260px 140px at 300px 150px, var(--stone-light), transparent 70%),
      radial-gradient(ellipse 220px 130px at 360px 560px, #e8d6bb, transparent 70%),
      radial-gradient(ellipse 180px 120px at 650px 620px, #d9bfa0, transparent 70%),
      radial-gradient(ellipse 200px 140px at 640px 120px, #d4b793, transparent 70%),
      linear-gradient(160deg, var(--stone-mid), var(--stone-dark));
  }
  .name-band {
    position: absolute;
    left: 0;
    top: 251px;
    width: 843px;
    height: 195px;
    background: var(--band);
  }
  .therapist-name {
    position: absolute;
    left: 26px;
    top: 250px;
    margin: 0;
    font-size: 112px;
    font-weight: 400;
    line-height: 1;
    letter-spacing: 8px;
    white-space: nowrap;
  }
  .therapist-title {
    position: absolute;
    left: 28px;
    top: 372px;
    margin: 0;
    font-size: 52px;
    font-weight: 400;
    line-height: 1;
    letter-spacing: 5px;
    white-space: nowrap;
  }
  .contact-line {
    position: absolute;
    left: 34px;
    top: 462px;
    margin: 0;
    font-size: 37px;
    line-height: 1;
    letter-spacing: 1px;
    white-space: nowrap;
    text-shadow: 0 1px 2px rgba(0, 0, 0, 0.4);
  }
  .specialty-panel {
    position: absolute;
    left: 843px;
    top: 0;
    width: 357px;
    height: 720px;
    background:
      radial-gradient(ellipse 160px 90px at 120px 80px, var(--panel-glow), transparent 75%),
      radial-gradient(ellipse 170px 110px at 260px 520px, var(--panel-glow), transparent 75%),
      linear-gradient(180deg, var(--panel-top), var(--panel-bottom));
    box-shadow: -6px 0 12px rgba(0, 0, 0, 0.3);
  }
  .specialty-list {
    list-style: none;
    margin: 0;
    padding: 0;
    position: absolute;
    left: 51px;
    top: 130px;
  }
  .specialty-list li {
    font-size: 54px;
    line-height: 1;
    height: 101px;
    letter-spacing: 2px;
    white-space: nowrap;
  }
  .sport-icons {
    position: absolute;
    left: 37px;
    top: 626px;
    width: 296px;
    height: 76px;
  }
</style>
</head>
<body>
  <main class="card">
    <div class="pebble-field" role="img" aria-label="Photograph of smooth river pebbles in warm sand and taupe tones"></div>
    <div class="name-band"></div>
    <h1 class="therapist-name">GLEN HARWICK</h1>
    <p class="therapist-title">Licensed Massage Therapist</p>
    <p class="contact-line">p. 203-555-0147&nbsp; ~ e. gharwick@mailbrook.example</p>

    <aside class="specialty-panel">
      <ul class="specialty-list">
        <li>Swedish</li>
        <li>Deep Tissue</li>
        <li>Sports</li>
        <li>Hot Stone</li>
      </ul>
      <svg class="sport-icons" viewBox="0 0 296 76" aria-label="Run, swim and cycle icons">
        <g fill="none" stroke="var(--icon-tone)" stroke-width="5" stroke-linecap="round" stroke-linejoin="round">
          <rect x="6" y="8" width="78" height="60" rx="30" fill="var(--icon-tone)" opacity="0.55" stroke="none" role="img" aria-label="Runner pictogram"/>
          <path d="M96 30 q10 -8 20 0 t20 0 t20 0 t20 0"/>
          <path d="M96 46 q10 -8 20 0 t20 0 t20 0 t20 0"/>
          <path d="M96 62 q10 -8 20 0 t20 0 t20 0 t20 0"/>
          <circle cx="212" cy="52" r="19"/>
          <circle cx="270" cy="52" r="19"/>
          <path d="M212 52 L232 26 L258 26 L270 52 M232 26 L244 52 L212 52 M244 52 L258 26"/>
        </g>
      </svg>
    </aside>
  </main>
</body>
</html>
```